We are a doctors medical practice
I need the business card to be eye catching and memorable,
to reflect professionalism, yet also warmth and care

the numbers need to be easy to see, for the elderly

and the logo also in a location that is large enough to see and be eye catching

Back of card:
opening hours:
Mon- Fri 8.30am to 6pm
Sat 9am to 4pm

rows for appontments, date and time
Updates

HiĀ 

Modification to company name

BRAMBLEWOOD HOME HEALTH MEDICAL PRACTICE

Thanks
Clara

Reason: I am look for a unique design that also fulfils the design brief

I have attempted to post a .eps and .ai file of the logo

Target Market(s)

needs to appeal to the majority, mainly adults

Industry/Entity Type

Medical

Contact Information for Business Card

company name: Bramblewood Home Health Medical Practice
Name: Dr Clara Ostrowski-Vey
Qualifications: MBBS, Bsci(med), FRACGP, DCH, SH&FPA, Dip Derm
Address: Shop 3/41-43 Calder Rd, Brookvale 2371
Ph: 02 9418 3052
Fax: 02 9436 8120

Requirements
Nice to have
• I like balance
gold/ silver incorporated, as well as the other colours in the logo- but not limited to these colours
a "medical" feel
Should not have
• dark or strong colours

```html
<!DOCTYPE html>
<html lang="en">
<head>
<meta charset="utf-8">
<title>Bramblewood Home Health Medical Practice – Appointment Card</title>
<link rel="stylesheet" href="https://fonts.googleapis.com/css2?family=Tinos:wght@400;700&family=Arimo:wght@400;700&display=swap">
<style>
  :root {
    --card: #f7f7f8;
    --stripe: #ecedf0;
    --ink: #111418;
    --navy: #1c2340;
    --blue: #2f5fb3;
    --rule-grey: #9aa3b0;
    --band-grey: #c9ced6;
    --teal: #2fa7b8;
    --green: #5bb84a;
  }
  * { margin: 0; padding: 0; box-sizing: border-box; }
  html, body { width: 1200px; height: 833px; overflow: hidden; background: #ffffff; }
  .card {
    position: relative;
    width: 1200px; height: 833px;
    background: repeating-linear-gradient(90deg, var(--card) 0 6px, var(--stripe) 6px 8px);
    font-family: "Tinos", "Times New Roman", serif;
    color: var(--ink);
  }
  .card-frame {
    position: absolute; inset: 28px;
    border: 5px solid var(--ink);
  }
  .brand-mark {
    position: absolute; left: 52px; top: 62px;
    width: 240px; height: 240px;
    display: flex; align-items: center; justify-content: center;
  }
  .brand-mark svg { position: absolute; inset: 0; }
  .brand-name {
    position: relative;
    width: 170px; text-align: center;
    font-size: 26px; line-height: 1.15;
    color: var(--teal);
  }
  .practice-name {
    position: absolute; left: 320px; top: 58px; width: 840px;
    text-align: center; font-size: 37px; color: var(--navy);
  }
  .doctor-name {
    position: absolute; left: 320px; top: 104px; width: 840px;
    text-align: center; font-size: 36px; color: var(--navy);
  }
  .hours-title {
    position: absolute; left: 470px; top: 172px; width: 480px; height: 60px;
    border-top: 8px solid var(--band-grey);
    border-bottom: 8px solid var(--band-grey);
    text-align: center; font-family: "Arimo", Arial, sans-serif;
    font-size: 34px; line-height: 44px; color: var(--blue);
  }
  .hours-title span { border-bottom: 2px solid var(--blue); }
  .hours-list {
    position: absolute; left: 420px; top: 250px; width: 580px;
    text-align: center; font-size: 31px; line-height: 40px; color: var(--ink);
  }
  .appointment-row {
    position: absolute; display: flex; align-items: flex-end;
    font-size: 46px; color: var(--ink);
  }
  .appointment-row .fill-line {
    flex: 1; margin-left: 12px; margin-bottom: 8px;
    border-bottom: 3px solid var(--ink);
  }
  .row-date { left: 60px; top: 410px; width: 1020px; }
  .row-time { left: 330px; top: 490px; width: 750px; }
  .contact-band {
    position: absolute; left: 110px; top: 608px; width: 980px; height: 54px;
    display: flex; justify-content: space-between;
  }
  .contact-box {
    width: 430px; height: 54px;
    border-top: 9px solid var(--band-grey);
    border-bottom: 9px solid var(--band-grey);
    text-align: center; font-family: "Arimo", Arial, sans-serif;
    font-size: 30px; line-height: 36px; color: var(--blue);
    letter-spacing: 1px;
  }
  .address {
    position: absolute; left: 40px; top: 690px; width: 1120px;
    text-align: center; font-family: "Arimo", Arial, sans-serif;
    font-weight: 700; font-size: 50px; color: var(--ink);
    letter-spacing: 1px;
  }
</style>
</head>
<body>
  <main class="card">
    <div class="card-frame"></div>

    <div class="brand-mark">
      <svg viewBox="0 0 240 240" aria-hidden="true">
        <circle cx="120" cy="120" r="110" fill="none" stroke="var(--teal)" stroke-width="14"/>
      </svg>
      <div class="brand-name">Bramblewood Home Health</div>
    </div>

    <h1 class="practice-name">Bramblewood Home Health Medical Practice</h1>
    <p class="doctor-name">Dr. Clara Ostrowski-Vey</p>

    <h2 class="hours-title"><span>Hours Of Operation</span></h2>
    <div class="hours-list">
      <p>Monday - Friday : 8:30AM-6:00PM</p>
      <p>Saturday: 9:00AM - 4:00PM</p>
    </div>

    <div class="appointment-row row-date">Appointment Date:<span class="fill-line"></span></div>
    <div class="appointment-row row-time">Time:<span class="fill-line"></span></div>

    <div class="contact-band">
      <p class="contact-box">FAX: 02 9436 8120</p>
      <p class="contact-box">Ph: 02 9418 3052</p>
    </div>

    <p class="address">3/41-43 Calder Rd. Brookvale 2371</p>
  </main>
</body>
</html>
```